Quorvex - Automated robotic Inspection with AI need new business cards

We need a new design of our business cards. The company is focused on automated quality control at high speed with unmatched results. We have a logo but need a more forward leaning business card that shows that we are delivering cutting edge technology.

Contact Information for Business Card

Name
Position
Adress
Phone
Email
e.g.
Lena Holmqvist
Chief Financial Officer (CFO)

Quorvex Sweden AB
Bruksvägen 14, SE-175 43 JÄRFÄLLA, Sweden
Mobile: +46735 21 47 83 | Office: +46 8 61 94 27
www.quorvex-example.com

Font styles to use
Sans Serif

```html
<!DOCTYPE html>
<html lang="en">
<head>
<meta charset="utf-8">
<title>Quorvex business cards</title>
<link rel="stylesheet" href="https://fonts.googleapis.com/css2?family=Michroma&family=Didact+Gothic&family=Open+Sans:wght@400&display=swap">
<style>
  :root {
    --stage: #2a2a2a;
    --brand-blue: #1c5686;
    --ink-blue: #1d5a8c;
    --paper: #ffffff;
    --grey-text: #8a8d91;
    --rule: #1d5a8c;
  }
  * { box-sizing: border-box; margin: 0; padding: 0; }
  html, body { width: 1200px; height: 900px; overflow: hidden; }
  body {
    background: var(--stage);
    position: relative;
    font-family: "Open Sans", sans-serif;
  }
  .card {
    position: absolute;
    left: 250px;
    width: 700px;
    height: 400px;
    box-shadow: 0 10px 30px rgba(0,0,0,.45);
  }
  .card--front { top: 35px; background: var(--brand-blue); }
  .card--back  { top: 465px; background: var(--paper); }

  .wordmark {
    position: absolute;
    left: 0; right: 0;
    text-align: center;
    font-family: "Michroma", sans-serif;
    letter-spacing: 4px;
  }
  .wordmark__name { display: block; font-size: 48px; line-height: 1; }
  .wordmark__tagline {
    display: block;
    font-family: "Open Sans", sans-serif;
    font-size: 13px;
    letter-spacing: 5px;
    margin-top: 10px;
  }
  .card--front .wordmark { top: 150px; color: var(--paper); }
  .card--back .wordmark { top: 55px; color: var(--ink-blue); }

  .holder {
    position: absolute;
    left: 70px; top: 215px;
    width: 280px;
    text-align: right;
  }
  .holder__name {
    font-family: "Michroma", sans-serif;
    font-size: 18px;
    letter-spacing: 2px;
    color: var(--ink-blue);
    white-space: nowrap;
  }
  .holder__role {
    font-family: "Didact Gothic", sans-serif;
    font-size: 17px;
    color: var(--grey-text);
    margin-top: 4px;
    white-space: nowrap;
  }
  .divider {
    position: absolute;
    left: 372px; top: 212px;
    width: 2px; height: 95px;
    background: var(--rule);
  }
  .contacts {
    position: absolute;
    left: 395px; top: 210px;
    list-style: none;
  }
  .contacts li {
    display: flex;
    align-items: center;
    gap: 12px;
    font-size: 17px;
    line-height: 25px;
    color: var(--grey-text);
    white-space: nowrap;
  }
  .contacts svg { width: 16px; height: 16px; fill: var(--ink-blue); flex: none; }

  .footer {
    position: absolute;
    left: 0; right: 0; bottom: 40px;
    display: flex;
    align-items: center;
    gap: 12px;
    font-family: "Didact Gothic", sans-serif;
    font-size: 16px;
    color: var(--grey-text);
    white-space: nowrap;
  }
  .footer__rule { flex: 1; height: 1.5px; background: var(--rule); }
  .footer__text { display: flex; align-items: center; }
  .footer__sep { color: var(--ink-blue); margin: 0 8px; }
</style>
</head>
<body>
  <section class="card card--front">
    <div class="wordmark">
      <span class="wordmark__name">QUORVEX</span>
      <span class="wordmark__tagline">Automated Robotic Inspection</span>
    </div>
  </section>

  <section class="card card--back">
    <div class="wordmark">
      <span class="wordmark__name">QUORVEX</span>
      <span class="wordmark__tagline">Automated Robotic Inspection</span>
    </div>

    <div class="holder">
      <p class="holder__name">LENA HOLMQVIST</p>
      <p class="holder__role">Chief Financial Officer (CFO)</p>
    </div>

    <div class="divider"></div>

    <ul class="contacts">
      <li>
        <svg viewBox="0 0 16 16" aria-hidden="true"><path d="M3.5 1l2.5 3-1.4 1.6c.9 2 2.4 3.5 4.3 4.4L10.5 8.5l3 2.5-1.2 2.6C7 13.5 2.5 9 2.4 3.2z"/></svg>
        +46 8 61 94 27
      </li>
      <li>
        <svg viewBox="0 0 16 16" aria-hidden="true"><path d="M5 1h6a1 1 0 0 1 1 1v12a1 1 0 0 1-1 1H5a1 1 0 0 1-1-1V2a1 1 0 0 1 1-1zm.5 2v9h5V3zM8 12.6a.7.7 0 1 0 0 1.4.7.7 0 0 0 0-1.4z"/></svg>
        +46735 21 47 83
      </li>
      <li>
        <svg viewBox="0 0 16 16" aria-hidden="true"><path d="M1 3h14v10H1zm1.5 1.3v.2L8 8.6l5.5-4.1v-.2zM2.5 6.2V11.7h11V6.2L8 10.3z"/></svg>
        info@quorvex-example.com
      </li>
      <li>
        <svg viewBox="0 0 16 16" aria-hidden="true"><path d="M8 1a7 7 0 1 0 0 14A7 7 0 0 0 8 1zm0 1.4c.8.7 1.5 2 1.8 3.6H6.2C6.5 4.4 7.2 3.1 8 2.4zM2.5 7.2h2.6c0 .6 0 1.1.1 1.6H2.5a5.6 5.6 0 0 1 0-1.6zm3.8 0h3.4a8 8 0 0 1 0 1.6H6.3a8 8 0 0 1 0-1.6zm4.6 0h2.6a5.6 5.6 0 0 1 0 1.6h-2.6l.1-1.6zM6.2 10h3.6c-.3 1.6-1 2.9-1.8 3.6-.8-.7-1.5-2-1.8-3.6z"/></svg>
        www.quorvex-example.com
      </li>
    </ul>

    <div class="footer">
      <span class="footer__rule"></span>
      <span class="footer__text">
        <span>Quorvex Sweden AB</span><span class="footer__sep">|</span><span>Bruksvägen 14, SE-175 43 JÄRFÄLLA</span><span class="footer__sep">|</span><span>SWEDEN</span>
      </span>
      <span class="footer__rule"></span>
    </div>
  </section>
</body>
</html>
```